Varlow's Electrical & Solar - Business Cards

I want my business card to stand out from the rest. I will provide my business name logo and my icon logo to be implemented onto the card.

On the front of the card, can i have the following. Just make it neat & professional please.

Dean Harrop
varlowselectrical@mailbox-example.net
0491 837 562
ABN: 41 269 507 813
License No. 582146K
FREE QUOTES
24/7 Emergency

On the back of the card, can I have "Our Services" and maybe add the V logo on the back in the background or something. Under "Our Services" I want the following:

LED Lighting Upgrades
Switches & Outlets
Smoke Alarms
Switchboard Upgrades
Fault Finding
Rewiring
New Builds
Test & Tagging
All Electrical Maintenance & Repairs

Can you guys add the instagram logo and next to it, put varlows_electrical

Can you guys also add the facebook logo and next to it put Varlow's Electrical & Solar. Make sure the instagram & facebook icon is in either white, green or black.

Also I have put down double sided, not sure why when i save it, it keeps going to single sided. I need my business card double sided.

New Customers

Dean Harrop varlowselectrical@mailbox-example.net 0491 837 562 ABN: 41 269 507 813 License No. 582146K FREE QUOTES 24/7 Emergency

• must be tidy, professional and appealing

```html
<!DOCTYPE html>
<html lang="en">
<head>
<meta charset="UTF-8">
<title>Varlow's Electrical &amp; Solar – Business Cards</title>
<link href="https://fonts.googleapis.com/css2?family=Open+Sans:wght@400;600&display=swap" rel="stylesheet">
<style>
  :root {
    --backdrop: #2a2c30;
    --card: #0b0b0c;
    --card-edge: #1a1b1d;
    --green: #2ebd4e;
    --white: #f2f2f2;
    --grey: #d8d8d8;
  }
  * { margin: 0; padding: 0; box-sizing: border-box; }
  html, body {
    width: 1200px; height: 900px; overflow: hidden;
    background: var(--backdrop);
    font-family: "Open Sans", sans-serif;
  }
  .canvas {
    width: 1200px; height: 900px;
    display: flex; flex-direction: column;
    align-items: center; justify-content: center; gap: 56px;
  }
  .card {
    width: 640px; height: 366px;
    background: var(--card);
    border: 1px solid var(--card-edge);
    border-radius: 4px;
    box-shadow: 0 14px 34px rgba(0,0,0,0.55);
    display: flex; align-items: center;
    padding: 0 48px;
    position: relative;
  }
  .brand {
    width: 220px;
    display: flex; flex-direction: column; align-items: center; gap: 14px;
    text-align: center;
  }
  .brand-mark {
    width: 46px; height: 46px; border-radius: 50%;
    background: var(--green);
  }
  .brand-name {
    color: var(--white);
    font-weight: 600; font-size: 19px; line-height: 1.3;
  }
  .divider {
    width: 2px; height: 200px; background: var(--white);
    margin: 0 36px 0 30px;
  }
  .details { display: flex; flex-direction: column; gap: 4px; }
  .person-name {
    color: var(--green); font-size: 25px; font-weight: 600;
    letter-spacing: 0.5px; text-transform: uppercase; margin-bottom: 10px;
  }
  .line {
    color: var(--white); font-size: 15.5px; line-height: 1.4;
    display: flex; align-items: center; gap: 8px;
  }
  .line svg { width: 13px; height: 13px; flex: none; }
  .gap { height: 8px; }
  .line.highlight { color: var(--green); font-weight: 600; }

  .card-back { flex-direction: column; align-items: stretch; justify-content: center; padding: 0 48px; }
  .back-main { display: flex; align-items: center; }
  .services { list-style: none; display: flex; flex-direction: column; gap: 3px; }
  .services li {
    color: var(--white); font-size: 15px; line-height: 1.35;
    display: flex; align-items: center; gap: 10px;
  }
  .services li::before {
    content: ""; width: 9px; height: 9px; border-radius: 50%;
    background: var(--green); flex: none;
  }
  .socials {
    display: flex; gap: 34px; margin-top: 26px; padding-left: 20px;
  }
  .social {
    color: var(--grey); font-size: 14px;
    display: flex; align-items: center; gap: 8px;
  }
  .social-dot { width: 12px; height: 12px; border-radius: 50%; background: var(--green); }
</style>
</head>
<body>
<main class="canvas">
  <section class="card card-front" aria-label="Front of card">
    <div class="brand">
      <span class="brand-mark"></span>
      <span class="brand-name">Varlow's Electrical &amp; Solar</span>
    </div>
    <div class="divider"></div>
    <div class="details">
      <h1 class="person-name">Dean Harrop</h1>
      <p class="line">
        <svg viewBox="0 0 24 24" aria-hidden="true"><path fill="#2ebd4e" d="M6.6 10.8a15 15 0 0 0 6.6 6.6l2.2-2.2a1 1 0 0 1 1-.25 11.4 11.4 0 0 0 3.6.57 1 1 0 0 1 1 1V20a1 1 0 0 1-1 1A17 17 0 0 1 3 4a1 1 0 0 1 1-1h3.5a1 1 0 0 1 1 1c0 1.25.2 2.45.57 3.57a1 1 0 0 1-.25 1z"/></svg>
        0491 837 562
      </p>
      <p class="line">
        <svg viewBox="0 0 24 24" aria-hidden="true"><rect x="2" y="5" width="20" height="14" rx="1.5" fill="#2ebd4e"/><path d="M3 6.5l9 6.5 9-6.5" fill="none" stroke="#0b0b0c" stroke-width="1.8"/></svg>
        varlowselectrical@mailbox-example.net
      </p>
      <div class="gap"></div>
      <p class="line">ABN: 41 269 507 813</p>
      <p class="line">License No. 582146K</p>
      <p class="line highlight">FREE QUOTES</p>
      <p class="line highlight">24/7 Emergency</p>
    </div>
  </section>

  <section class="card card-back" aria-label="Back of card">
    <div class="back-main">
      <div class="brand">
        <span class="brand-mark"></span>
        <span class="brand-name">Varlow's Electrical &amp; Solar</span>
      </div>
      <div class="divider"></div>
      <ul class="services">
        <li>LED Lighting Upgrades</li>
        <li>Switches &amp; Outlets</li>
        <li>Smoke Alarms</li>
        <li>Switchboard Upgrades</li>
        <li>Fault Finding</li>
        <li>Rewiring</li>
        <li>New Builds</li>
        <li>Test &amp; Tagging</li>
        <li>All Electrical Maintenance &amp; Repairs</li>
      </ul>
    </div>
    <div class="socials">
      <span class="social"><span class="social-dot"></span>varlows_electrical</span>
      <span class="social"><span class="social-dot"></span>Varlow's Electrical &amp; Solar</span>
    </div>
  </section>
</main>
</body>
</html>
```